Workers comp/Business Ins/ Payroll- Postcard

I own an insurance agency.  I'm interested in getting some professional advice on how to design a message for what i want to sell.  The products I want to sell are 1) Workers compensation 2) business Insurance 3) Payroll processing. They are integrated together but I'm not sure if it's too much to put on a postcard and if I don't put it on a postcard I could be missing out on sales.
I have the ability to look up what Insurance company a business has their workers compensation  policy with, along with their expiration date.  Based on that information I can tell if the business is overpaying for their Workers compensation. insurance. Most companies are overpaying so I can usually save a company money very quickly if I can get in front of them. Some businesses work with a broker such as myself and buy a policy. When it's done this way, the business ESTIMATES his payroll for the year and at the end of the year they have to complete an audit to find out the actual payroll. Based on audit, they will either owe more money if they were low or get money back if they were high. The other way a business buys a workers comp. policy is with their payroll company. The payroll company will place the policy on Pay -as- you -go which means when you pay your employees every week they  will also calculate how much the workers comp premium is for the week and take that amount out of their checking account. This method avoids large down payments, helps with cash flow and should be very accurate at the end of the policy term.  This is by far the best way to do this for the businessowner. My company also has payroll company and we do this for the insured as well. However, most payroll company's such as QRT and Wagelon charge the customer $15 every time they do this so if it's weekly it is another $780 a year.  We also complete the insured's audit for them which is a big headache for the businessowner.
One of our biggest benefits of doing business with our company is we have a  Steady Rate Forever. When you sign up your base price will never increase. Payroll companies are famous for "discounting a new client" only to increase the rate in a few months later. Our service is also superior to the other payroll companies who use overseas service centers. We have staff within our office and we can answer questions quickly. We usually save businesses money on  their Payroll processing but it's not what we focus on- We focus on the Service.
Business Insurance- One of our main companies that we represent is Brindle Insurance. Brindle is very competitive and we usually write business accounts where we save the business owner money but offer superior coverages.
in summary, I'm offering 1) better workers compensation rates 2) Pay as you go workers comp. 3) Steady Rate, audits done for you, and superior customer service with our payroll company 4) savings on their business insurance with superior coverages.
Sometimes when we talk to an insured we may start with just their payroll and later get the WC and business liability. Each account is different and we do not pressure people to make decisions and we do what is right for them.  The biggest takeaway is we take some things off the plate for the businessowner where they can make just one phone call to get what they need done.  Our Website is www.harbor-mutual.example. my email is tomk@harbor-mutual.example if you have any questions.
Thank You
Tom Kessor

Target Market(s)
Small business owners 1-50 employees
Industry/Entity Type
Insurance and Payroll
Font styles to use
Other font styles liked:
- Let designer choose

Colors
Designer to choose colors to be used in the design.
Requirements
Must have
- It shouldn't be boring- needs to stand out- can use 6x11 inch postcard

Nice to have
- I like humor but not a must

Should not have
- Nothing I can think of

```html
<!DOCTYPE html>
<html lang="en">
<head>
<meta charset="utf-8">
<title>Harbor Mutual – Workers Comp, Payroll &amp; Business Insurance Postcard</title>
<link rel="stylesheet" href="https://fonts.googleapis.com/css2?family=Bebas+Neue&family=Josefin+Sans:wght@400;700&family=Montserrat:wght@400;700&display=swap">
<style>
  :root {
    --brand-red: #7a2c30;
    --brand-grey: #87888a;
    --page-bg: #bcbdc0;
    --ink: #1f1f1f;
    --paper: #ffffff;
    --soft-grey: #e9e9ea;
    --chev-1: #f0f0f2;
    --chev-2: #e5e5e7;
    --chev-3: #d3d4d6;
  }
  * { box-sizing: border-box; margin: 0; padding: 0; }
  html, body { width: 1076px; height: 1200px; overflow: hidden; }
  body { background: var(--page-bg); position: relative; font-family: "Montserrat", sans-serif; }

  .card { position: absolute; left: 74px; width: 928px; background: var(--paper); box-shadow: 0 3px 8px rgba(0,0,0,.18); overflow: hidden; }
  .card-front { top: 74px; height: 505px; }
  .card-back { top: 619px; height: 507px; }
  .card-shapes { position: absolute; inset: 0; width: 100%; height: 100%; }
  .abs { position: absolute; white-space: nowrap; line-height: 1; }
  .center { transform: translateX(-50%); text-align: center; }

  /* Front */
  .headline { left: 0; width: 928px; text-align: center; font-family: "Bebas Neue", sans-serif; font-size: 80px; color: var(--brand-grey); }
  .headline .accent { color: var(--brand-red); }
  .headline-1 { top: 7px; }
  .headline-2 { top: 78px; }
  .promise-banner { top: 164px; left: 0; width: 928px; line-height: 48px; text-align: center; font-family: "Josefin Sans", sans-serif; font-weight: 700; font-size: 25px; color: var(--paper); letter-spacing: .5px; }
  .art { position: absolute; }
  .art-stressed { left: 15px; top: 219px; width: 251px; height: 198px; background: linear-gradient(160deg, #eef3fa, #c9dcef 60%, #e8e6e3); border-radius: 6px; }
  .art-relaxed { left: 674px; top: 219px; width: 254px; height: 196px; background: linear-gradient(200deg, #f4f6f9, #bcd4ee 55%, #4b5f7e); border-radius: 6px 0 0 0; }
  .offer { font-family: "Bebas Neue", sans-serif; color: var(--paper); }
  .offer-free { left: 502px; top: 240px; font-size: 56px; }
  .offer-analysis { left: 465px; top: 302px; font-size: 60px; }
  .no-pressure { left: 452px; top: 368px; font-family: "Josefin Sans", sans-serif; font-size: 26px; color: var(--ink); }
  .brand-name { font-family: "Josefin Sans", sans-serif; font-weight: 700; color: var(--brand-red); }
  .front-brand { left: 40px; top: 446px; font-size: 42px; }
  .contact { right: 18px; text-align: right; font-family: "Josefin Sans", sans-serif; font-size: 30px; color: var(--paper); }
  .contact b { font-weight: 700; }
  .contact-call { top: 430px; }
  .contact-web { top: 463px; font-size: 29px; }

  /* Back */
  .back-headline { left: 25px; top: 34px; font-family: "Bebas Neue", sans-serif; font-size: 78px; color: var(--paper); }
  .win-title { top: 201px; font-family: "Bebas Neue", sans-serif; font-size: 28px; color: var(--paper); }
  .win-text { top: 230px; font-size: 12.5px; line-height: 18px; color: var(--paper); }
  .win-1 { left: 127px; } .win-2 { left: 355px; } .win-3 { left: 573px; }
  .why-us { left: 22px; top: 287px; width: 640px; white-space: normal; font-size: 13px; line-height: 19px; color: var(--paper); }
  .why-us b { font-weight: 700; }
  .benefit { display: flex; align-items: center; gap: 5px; font-family: "Bebas Neue", sans-serif; font-size: 26px; color: var(--paper); }
  .benefit svg { width: 20px; height: 20px; flex: none; }
  .benefit-r1 { top: 346px; } .benefit-r2 { top: 377px; }
  .benefit-c1 { left: 22px; } .benefit-c2 { left: 317px; }
  .lines-of-cover { left: 375px; top: 429px; font-family: "Bebas Neue", sans-serif; font-size: 25px; color: var(--paper); }
  .address { left: 375px; font-size: 14px; color: var(--paper); }
  .address-1 { top: 461px; } .address-2 { top: 481px; }
  .back-brand { left: 18px; top: 458px; font-size: 25px; }
</style>
</head>
<body>

<section class="card card-front" aria-label="Postcard front">
  <svg class="card-shapes" viewBox="0 0 1570 855" preserveAspectRatio="none" aria-hidden="true">
    <rect x="0" y="278" width="1570" height="80" fill="var(--brand-grey)"/>
    <polygon points="0,278 1570,278 1500,358 70,358" fill="var(--brand-red)"/>
    <polygon points="675,397 1110,397 1020,500 597,500" fill="var(--brand-red)"/>
    <polygon points="510,510 1157,510 1070,612 420,612" fill="var(--brand-grey)"/>
    <defs>
      <linearGradient id="brandBand" x1="0" x2="1" y1="0" y2="0">
        <stop offset="0" stop-color="#e6e6e7"/>
        <stop offset="1" stop-color="#ffffff"/>
      </linearGradient>
    </defs>
    <rect x="0" y="703" width="900" height="152" fill="url(#brandBand)"/>
    <polygon points="905,703 1570,703 1570,855 768,855" fill="var(--brand-red)"/>
  </svg>

  <h1 class="abs headline headline-1"><span class="accent">Tired of overpaying</span> for workers</h1>
  <div class="abs headline headline-2">comp, payroll, and <span class="accent">insurance?</span></div>
  <p class="abs promise-banner">Harbor Mutual makes it EASY, AFFORDABLE, and HASSLE-FREE</p>

  <div class="art art-stressed" role="img" aria-label="Illustration of a stressed business owner with a calculator, flying papers and a clock"></div>
  <div class="art art-relaxed" role="img" aria-label="Illustration of a relaxed business owner sitting in an office chair holding a coffee mug"></div>

  <div class="abs offer offer-free center">Get a free</div>
  <div class="abs offer offer-analysis center">Savings analysis!</div>
  <p class="abs no-pressure center">(No pressure. No obligation)</p>

  <div class="abs brand-name front-brand">HARBOR MUTUAL</div>

  <p class="abs contact contact-call">Call Tom at <b>555-010-2846</b></p>
  <p class="abs contact contact-web">www.<b>harbor-mutual</b>.example</p>
</section>

<section class="card card-back" aria-label="Postcard back">
  <svg class="card-shapes" viewBox="0 0 1570 857" preserveAspectRatio="none" aria-hidden="true">
    <polygon points="0,0 1565,0 1490,80 1215,80 1215,392 1150,467 0,467" fill="var(--brand-red)"/>
    <polygon points="0,467 1150,467 1070,564 0,564" fill="var(--brand-grey)"/>
    <polygon points="0,564 1060,564 935,702 0,702" fill="var(--brand-red)"/>
    <polygon points="337,702 935,702 803,857 472,857" fill="var(--brand-grey)"/>
    <rect x="1215" y="80" width="278" height="312" fill="var(--paper)" stroke="#9a9b9d" stroke-width="3"/>
    <g stroke="#8c8d8f" stroke-width="3">
      <line x1="1180" y1="519" x2="1490" y2="519"/>
      <line x1="1065" y1="649" x2="1490" y2="649"/>
      <line x1="952" y1="777" x2="1490" y2="777"/>
    </g>
    <polygon points="45,200 385,200 420,263 385,327 45,327 80,263" fill="var(--chev-1)"/>
    <polygon points="413,200 755,200 790,263 755,327 413,327 448,263" fill="var(--chev-2)"/>
    <polygon points="780,200 1125,200 1160,263 1125,327 780,327 815,263" fill="var(--chev-3)"/>
    <g fill="var(--ink)">
      <path d="M218,222 L250,234 V264 Q250,292 218,307 Q186,292 186,264 V234 Z"/>
      <circle cx="600" cy="263" r="44"/>
      <path d="M970,222 L1002,234 V264 Q1002,292 970,307 Q938,292 938,264 V234 Z" fill="none" stroke="var(--ink)" stroke-width="7"/>
    </g>
    <polyline points="204,263 214,275 234,250" fill="none" stroke="var(--paper)" stroke-width="7"/>
    <text x="600" y="281" text-anchor="middle" font-family="Montserrat, sans-serif" font-weight="700" font-size="50" fill="var(--paper)">$</text>
    <polyline points="956,263 966,275 986,250" fill="none" stroke="var(--ink)" stroke-width="7"/>
  </svg>

  <h2 class="abs back-headline">One call. Three big wins.</h2>

  <h3 class="abs win-title win-1 center">Workers Compensation</h3>
  <p class="abs win-text win-1 center">Save big with<br>Pay-As-You-Go plans.</p>
  <h3 class="abs win-title win-2 center">Payroll Services</h3>
  <p class="abs win-text win-2 center">Steady Rate for Life.<br>No rate hikes. Local support.</p>
  <h3 class="abs win-title win-3 center">Business Insurance</h3>
  <p class="abs win-text win-3 center">Better coverage.<br>Lower rates. Trusted carriers.</p>

  <p class="abs why-us">Business owners overpay because they don't know better options exist. Harbor Mutual gives you <b>better rates, local service, and peace of mind</b> - without the big corporate headaches.</p>

  <div class="abs benefit benefit-r1 benefit-c1"><svg viewBox="0 0 20 20" aria-hidden="true"><polyline points="2,11 8,18 19,2" fill="none" stroke="#fff" stroke-width="3.5"/></svg>Lower workers comp premiums</div>
  <div class="abs benefit benefit-r1 benefit-c2"><svg viewBox="0 0 20 20" aria-hidden="true"><polyline points="2,11 8,18 19,2" fill="none" stroke="#fff" stroke-width="3.5"/></svg>Faster service - no offshore</div>
  <div class="abs benefit benefit-r2 benefit-c1"><svg viewBox="0 0 20 20" aria-hidden="true"><polyline points="2,11 8,18 19,2" fill="none" stroke="#fff" stroke-width="3.5"/></svg>No big deposits — pay-as-you-go</div>
  <div class="abs benefit benefit-r2 benefit-c2"><svg viewBox="0 0 20 20" aria-hidden="true"><polyline points="2,11 8,18 19,2" fill="none" stroke="#fff" stroke-width="3.5"/></svg>Audit help - we handle it.</div>

  <div class="abs brand-name back-brand">HARBOR MUTUAL</div>

  <p class="abs lines-of-cover center">Auto • Home • Business • Payroll</p>
  <p class="abs address address-1 center">820 Linden Hollow Road, Westbrook</p>
  <p class="abs address address-2 center">NY 14000</p>
</section>

</body>
</html>
```